Professional and stylish textiles catalogue

Wool throws and cushions product catalogue.
Target audience are business customers (interior stores). Besides providing information about products the catalogue must able to sell, therefore we expect it to be professional and stylish.
Size A5 horizontal.
Content:
1. Cover: Logo and 2011/12 on front, company details on reverse;
2. Page with photo and short info about company;
3. Product pages spread - one item per page. Total 15 double-page spreads;
4. Info page with photo and small text about gift packaging.
Products - throws and cushions. Located as a pair on each spread: throw on the left, cushion on the right. One double-page spread with three throws.
Products mostly are in natural colours: grey, beige and brown. Three throws/cushions in light shades of rose, green and blue.
Comments: catalogue must be in bright colours, could be white with colourful details. Will be great if each product's double-page spread will have stylish details (could be lines) in colours of the product located in this certain double-page spread.
Materials provided:
1. Texts;
2. White background pictures of each product;
3. Several product pictures taken in the interior to use for the cover;
4. Logo.
Complete set of pictures in high resolution will be provided on request.

```html
<!DOCTYPE html>
<html lang="en">
<head>
<meta charset="utf-8">
<title>Velana – About</title>
<link rel="stylesheet" href="https://fonts.googleapis.com/css2?family=Marcellus&display=swap">
<style>
  :root {
    --page-bg: #ffffff;
    --ink: #2b2d33;
    --band: #434650;
    --band-text: #d9dadd;
    --cap-text: #ffffff;
    --photo-light: #efe6e0;
    --photo-mid: #b9a59a;
    --photo-dark: #6f5d55;
    --box-grey: #8d9092;
  }
  * { margin: 0; padding: 0; box-sizing: border-box; }
  html, body { width: 1200px; height: 846px; overflow: hidden; background: var(--page-bg); }
  .page {
    position: relative;
    width: 1200px;
    height: 846px;
    background: var(--page-bg);
    font-family: "Marcellus", "Optima", serif;
    color: var(--ink);
  }
  .product-photo {
    position: absolute;
    left: 20px;
    top: 262px;
    width: 765px;
    height: 372px;
    border-radius: 120px 40px 20px 60px;
    background:
      linear-gradient(100deg, rgba(255,255,255,0) 55%, var(--box-grey) 56%, #b7babc 80%, rgba(255,255,255,0) 81%),
      radial-gradient(ellipse at 45% 45%, var(--photo-dark) 0%, var(--photo-mid) 45%, var(--photo-light) 75%, rgba(255,255,255,0) 100%);
    opacity: 0.9;
  }
  .about {
    position: absolute;
    left: 820px;
    top: 34px;
    width: 353px;
    font-size: 17.6px;
    line-height: 24.3px;
    text-align: justify;
    text-align-last: justify;
  }
  .about p { margin-bottom: 48px; }
  .drop-cap {
    float: left;
    width: 71px;
    height: 102px;
    margin: -34px 5px 0 -10px;
    background: var(--band);
    color: var(--cap-text);
    font-size: 96px;
    line-height: 1;
    padding-top: 22px;
    text-align: center;
    text-align-last: center;
  }
  .footer-band {
    position: absolute;
    left: 0;
    bottom: 0;
    width: 1200px;
    height: 64px;
    background: var(--band);
  }
  .brand {
    position: absolute;
    left: 50%;
    top: 50%;
    transform: translate(-50%, -50%);
    display: flex;
    align-items: center;
    gap: 10px;
    color: var(--band-text);
    font-size: 27px;
    letter-spacing: 0.5px;
  }
  .brand-dot {
    width: 12px;
    height: 12px;
    border-radius: 50%;
    background: var(--band-text);
  }
  .page-number {
    position: absolute;
    right: 14px;
    bottom: 6px;
    color: var(--band-text);
    font-size: 12px;
  }
</style>
</head>
<body>
  <div class="page">
    <div class="product-photo" role="img" aria-label="Rolled brown and beige patterned alpaca throw with long fringe, resting on a grey gift box"></div>

    <div class="about">
      <p><span class="drop-cap">V</span>elana is a textile design company established in London in 2010 with the intention of creating high quality, environmentally friendly, handwoven throws and cushions.</p>
      <p>Values like beauty, long-lasting quality and harmony with nature, humans and objects lead to the creation of Velana accessories which are in classic designs, made with the environment in mind and sourced from sustainable materials.</p>
      <p>The 2011/12 collection is made from finest Peruvian baby alpaca, utilizing ancient Andean textile expertise and woven on traditional handlooms by professional handweavers in Peru.</p>
    </div>

    <footer class="footer-band">
      <div class="brand"><span class="brand-dot"></span><span class="brand-name">VELANA</span></div>
      <span class="page-number">3</span>
    </footer>
  </div>
</body>
</html>
```